North Fern Holdings Business Card

A business card design to accompany the logo design you completed on Artisan Hive. We are open to your proposals. I did add one idea below that might work, but we aren't married to the idea. The company is a real estate services company. Clientele are typically high net worth individuals, executive level employment or owners of their own company, 30-60 years old.

Our 1 (bad?) idea: double sided card; One side landscape with logo and word mark. Other side Portrait with the logo only (oversize watermark maybe?). Somewhere add text of Name (Marcus Pellington), Title (Principal), phone # (949-555-0173) and email address (marcus@northfernhq.com). There would be a second design with my wife's name, number and email in place of mine.

Again totally open to ideas here.

Industry/Entity Type

Real Estate

```html
<!DOCTYPE html>
<html lang="en">
<head>
<meta charset="utf-8">
<title>North Fern Holdings – Business Card</title>
<link href="https://fonts.googleapis.com/css2?family=Cinzel:wght@400&family=Arimo:wght@400;700&display=swap" rel="stylesheet">
<style>
  :root {
    --sage: #7f9f72;
    --sage-dark: #6f8f63;
    --rule-grey: #a6a6a6;
    --text-grey: #9a9a9a;
    --paper: #ffffff;
    --backdrop: #ececec;
  }
  * { margin: 0; padding: 0; box-sizing: border-box; }
  html, body { width: 1200px; height: 720px; overflow: hidden; }
  body { background: var(--backdrop); position: relative; font-family: "Arimo", Arial, sans-serif; }

  .card { position: absolute; background: var(--paper); box-shadow: 0 2px 6px rgba(0,0,0,0.12); overflow: hidden; }

  /* Back side – portrait with contact details */
  .card-back { left: 150px; top: 80px; width: 320px; height: 560px; }
  .card-back .sweep { position: absolute; inset: 0; width: 100%; height: 100%; }
  .back-mark { position: absolute; top: 70px; right: 34px; display: flex; flex-direction: column; align-items: center; gap: 12px; }
  .mark-dot { width: 74px; height: 74px; border-radius: 50%; background: var(--sage); }
  .back-mark .mark-name { font-family: "Cinzel", Georgia, serif; font-weight: 400; font-size: 13px; letter-spacing: 1px; color: var(--sage); }
  .contact { position: absolute; left: 28px; bottom: 46px; color: var(--paper); }
  .contact .person { font-weight: 700; font-size: 22px; letter-spacing: 0.3px; }
  .contact .role { font-size: 14px; margin-top: 4px; }
  .contact .line { font-size: 14px; margin-top: 14px; letter-spacing: 0.4px; }
  .contact .line + .line { margin-top: 6px; }

  /* Front side – landscape with name */
  .card-front { left: 540px; top: 200px; width: 560px; height: 320px; }
  .band { position: absolute; left: 0; right: 0; height: 44px; background: var(--sage); }
  .band-top { top: 0; }
  .band-bottom { bottom: 0; }
  .rule { position: absolute; left: 0; right: 0; height: 3px; background: var(--rule-grey); }
  .rule-top-a { top: 56px; } .rule-top-b { top: 64px; }
  .rule-bottom-a { bottom: 56px; } .rule-bottom-b { bottom: 64px; }
  .front-mark { position: absolute; top: 50%; left: 50%; transform: translate(-50%, -50%); display: flex; align-items: center; gap: 22px; white-space: nowrap; }
  .front-mark .mark-dot { width: 70px; height: 70px; }
  .front-mark .mark-name { font-family: "Cinzel", Georgia, serif; font-weight: 400; font-size: 32px; letter-spacing: 1.5px; color: var(--sage); }
</style>
</head>
<body>

  <section class="card card-back" aria-label="Card back">
    <svg class="sweep" viewBox="0 0 320 560" aria-hidden="true">
      <path d="M0 196 C150 200 276 268 320 386" fill="none" stroke="#a6a6a6" stroke-width="3"/>
      <path d="M0 206 C146 210 268 276 320 400" fill="none" stroke="#a6a6a6" stroke-width="3"/>
      <path d="M0 222 C142 226 262 292 320 420 L320 560 L0 560 Z" fill="#7f9f72"/>
    </svg>
    <div class="back-mark">
      <span class="mark-dot"></span>
      <span class="mark-name">North Fern Holdings</span>
    </div>
    <div class="contact">
      <p class="person">Marcus Pellington</p>
      <p class="role">Principal</p>
      <p class="line">949-555-0173</p>
      <p class="line">marcus@northfernhq.com</p>
    </div>
  </section>

  <section class="card card-front" aria-label="Card front">
    <div class="band band-top"></div>
    <div class="rule rule-top-a"></div>
    <div class="rule rule-top-b"></div>
    <div class="front-mark">
      <span class="mark-dot"></span>
      <span class="mark-name">North Fern Holdings</span>
    </div>
    <div class="rule rule-bottom-b"></div>
    <div class="rule rule-bottom-a"></div>
    <div class="band band-bottom"></div>
  </section>

</body>
</html>
```